nonprofit organization looking for sleek new design

We need a fresh new look for this nonprofit organization, Tidewater Allies for Learning and Mutual Aid, INC (TALMA, Inc.). This organization provides educational, nutritional, dental health, and specialized services to Cedar Step children, aiming to support families meeting federal income poverty guidelines. Our mission is clear: "Creating a brighter future for the children and la familia." We focus on child development, family wellness, staff growth, and community partnerships.

```html
<!DOCTYPE html>
<html lang="en">
<head>
<meta charset="utf-8">
<title>TALMA, Inc. — Tidewater Allies for Learning and Mutual Aid</title>
<link href="https://fonts.googleapis.com/css2?family=Montserrat:wght@500;600;700;800&family=Open+Sans:wght@400;600;700&display=swap" rel="stylesheet">
<style>
:root{
  --teal:#1fb89a;
  --teal-dark:#17957d;
  --ink:#1d1d1f;
  --body:#555a5e;
  --white:#ffffff;
  --footer:#1e1e1e;
  --footer-bar:#151515;
  --line:#e4e6e8;
  --star:#f4b400;
}
*{margin:0;padding:0;box-sizing:border-box}
html,body{width:1200px;height:3552px;overflow:hidden}
body{font-family:"Open Sans",sans-serif;color:var(--body);background:var(--white);position:relative}
h1,h2,h3,h4,.nav,.btn,.brand{font-family:"Montserrat",sans-serif}
.abs{position:absolute}

/* header */
.site-header{position:absolute;top:0;left:0;width:1200px;height:88px;background:var(--white);border-top:4px solid var(--teal)}
.brand{position:absolute;left:112px;top:22px;font-size:38px;font-weight:800;color:var(--ink);letter-spacing:1px}
.nav{position:absolute;left:396px;top:34px;display:flex;align-items:center;font-size:15px;font-weight:600;color:var(--ink)}
.nav span{padding:0 24px;border-right:1px solid #999;line-height:16px}
.nav span:last-child{border-right:none}
.btn{display:inline-block;background:var(--teal);color:var(--white);font-weight:700;font-size:14px;border-radius:20px;padding:9px 22px;letter-spacing:.5px}
.signup{position:absolute;left:972px;top:26px}

/* hero */
.hero{position:absolute;top:88px;left:0;width:1200px;height:652px;background:linear-gradient(110deg,#c9a58d 0%,#e9dccf 30%,#f0e3d6 50%,#9fb3bf 72%,#c8b59d 100%)}
.hero-shade{position:absolute;inset:0;background:linear-gradient(90deg,rgba(0,0,0,0) 45%,rgba(0,0,0,.28) 100%)}
.hero h1{position:absolute;left:628px;top:272px;font-size:46px;font-weight:800;color:var(--white);letter-spacing:1px}
.hero p{position:absolute;left:628px;top:340px;width:460px;color:var(--white);font-size:15px;line-height:22px}
.hero .btn{position:absolute;left:628px;top:420px}

/* mission */
.mission{position:absolute;top:740px;left:0;width:1200px;height:256px;background:var(--teal);text-align:center;color:var(--white)}
.mission h2{margin-top:58px;font-size:34px;font-weight:800;letter-spacing:1px}
.mission p{width:640px;margin:22px auto 0;font-size:15px;line-height:26px}

/* about */
.about-photo{position:absolute;left:96px;top:1060px;width:316px;height:316px;border-radius:50%;border:12px solid #dcdcdc;background:radial-gradient(circle at 45% 40%,#e8c7a6 0%,#d79f74 35%,#a9876b 70%,#8c7766 100%)}
.about h2{position:absolute;left:586px;top:1070px;font-size:36px;font-weight:800;color:var(--ink)}
.about .copy{position:absolute;left:586px;top:1132px;width:520px;font-size:13.5px;line-height:21px}
.about .copy p{margin-bottom:10px}
.about .btn{position:absolute;left:586px;top:1404px;font-size:13px;padding:7px 18px}

/* services */
.section-title{position:absolute;left:0;width:1200px;text-align:center;font-size:36px;font-weight:800;color:var(--ink)}
.services{position:absolute;left:0;top:1636px;width:1200px;height:334px;display:flex;gap:8px}
.service{flex:1;position:relative;overflow:hidden}
.service .fill{position:absolute;inset:0}
.service .scrim{position:absolute;inset:0;background:linear-gradient(180deg,rgba(0,0,0,0) 45%,rgba(0,0,0,.55) 100%)}
.service .label{position:absolute;left:0;right:0;bottom:26px;text-align:center;color:var(--white);font-family:"Montserrat",sans-serif;font-weight:700;font-size:19px}
.service svg{position:absolute;left:50%;bottom:60px;transform:translateX(-50%)}

/* testimonials */
.testimonial{position:absolute;top:2140px;width:316px;height:270px;background:var(--white);border-radius:8px;box-shadow:0 4px 18px rgba(0,0,0,.12);padding:22px 24px}
.testimonial p{font-size:13px;line-height:20px}
.testimonial .tag{margin-top:6px;font-size:12.5px;color:var(--teal);font-weight:600}
.person{display:flex;align-items:center;margin-top:14px}
.avatar{width:38px;height:38px;border-radius:50%;background:linear-gradient(135deg,#c79a78,#7d5b46)}
.person h4{font-size:15px;font-weight:700;color:var(--ink);margin-left:12px}
.stars{margin-left:12px;color:var(--star);font-size:14px;letter-spacing:1px}
.arrow{position:absolute;font-size:20px;color:var(--ink)}

/* blog */
.blog{position:absolute;top:2520px;left:0;width:1200px;height:650px;background:linear-gradient(180deg,#22bf9f,#1aa98c)}
.blog h2{position:absolute;top:78px;width:1200px;text-align:center;font-size:36px;font-weight:800;color:var(--white)}
.feature-photo{position:absolute;left:112px;top:168px;width:450px;height:272px;background:linear-gradient(135deg,#cfd8df,#e7c49c 50%,#b7a58d)}
.feature-card{position:absolute;left:112px;top:440px;width:450px;height:148px;background:var(--white);padding:18px 96px 0 22px}
.feature-card h3{font-size:17px;line-height:22px;font-weight:700;color:var(--ink)}
.feature-card p{font-size:12px;line-height:17px;margin-top:6px}
.feature-go{position:absolute;right:24px;top:50px;width:42px;height:42px;border-radius:50%;background:var(--teal)}
.post{position:absolute;left:632px;width:456px;height:196px;background:var(--white);display:flex}
.post .thumb{width:176px;height:100%}
.post .text{padding:18px 18px 0 20px;flex:1}
.date{font-size:12px;color:var(--teal);font-weight:600;display:flex;align-items:center;gap:6px}
.post h3{font-size:15.5px;line-height:20px;font-weight:700;color:var(--ink);margin-top:8px}
.post p{font-size:11.5px;line-height:16px;margin-top:6px}
.readmore{margin-top:8px;font-family:"Montserrat",sans-serif;font-size:12px;font-weight:700;color:var(--teal)}
.blog .side{position:absolute;top:300px;font-size:22px;color:var(--white)}

/* footer */
.site-footer{position:absolute;top:3170px;left:0;width:1200px;height:340px;background:var(--footer);color:#d8d8d8}
.site-footer .brand{left:112px;top:134px;color:var(--white);font-size:40px}
.site-footer h4{font-size:16px;font-weight:700;color:var(--white);letter-spacing:.5px}
.site-footer h4::after{content:"";display:block;width:34px;height:2px;background:var(--teal);margin-top:8px}
.col{position:absolute;top:60px}
.col ul{list-style:none;margin-top:22px;font-size:13px}
.col li{margin-bottom:12px}
.contact li{display:flex;align-items:flex-start;gap:10px}
.ico{flex:none;width:22px;height:22px;border-radius:50%;background:#3a3a3a;display:flex;align-items:center;justify-content:center}
.subscribe p{font-size:12.5px;line-height:18px;margin-top:20px;width:240px}
.field{margin-top:16px;width:250px;height:32px;background:var(--white);border-radius:16px;position:relative;font-size:11px;color:#999;padding:8px 14px}
.field .send{position:absolute;right:2px;top:2px;width:44px;height:28px;border-radius:14px;background:var(--teal)}
.socials{display:flex;gap:10px;margin-top:18px}
.socials span{width:28px;height:28px;border-radius:50%;background:var(--white)}
.socials span.on{background:var(--teal)}
.legal{position:absolute;top:3510px;left:0;width:1200px;height:42px;background:var(--footer-bar);font-size:12px;color:#cfcfcf}
.legal .left{position:absolute;left:112px;top:13px}
.legal .left b{color:var(--white);text-decoration:underline}
.legal .right{position:absolute;left:808px;top:13px;word-spacing:4px}
.chat{position:absolute;left:1126px;top:3454px;width:38px;height:38px;border-radius:50%;background:var(--teal)}
</style>
</head>
<body>

<header class="site-header">
  <div class="brand">TALMA</div>
  <nav class="nav"><span>HOME</span><span>ABOUT</span><span>SERVICES</span><span>BLOG</span><span>CONTACT</span></nav>
  <span class="btn signup">SIGN UP</span>
</header>

<section class="hero">
  <div class="abs" style="inset:0" role="img" aria-label="Photo of a smiling teacher helping a young girl paint in a bright classroom"></div>
  <div class="hero-shade"></div>
  <h1>WELCOME TO TALMA</h1>
  <p>Lorem ipsum dolor sit amet, consectetur adipiscing elit, sed do eiusmod tempor incididunt ut labore et dolore magna aliqua.</p>
  <span class="btn">LEARN MORE</span>
</section>

<section class="mission">
  <h2>OUR MISSION</h2>
  <p>Creating a brighter future for the children and la familia." We focus on child development, family wellness, staff growth, and community partnerships.</p>
</section>

<section class="about">
  <div class="about-photo" role="img" aria-label="Circular photo of a teacher playing with building blocks alongside young children"></div>
  <h2>ABOUT US</h2>
  <div class="copy">
    <p>Lorem ipsum dolor sit amet, consectetur adipiscing elit, sed do eiusmod tempor incididunt ut labore et dolore magna aliqua. Ut enim ad minim veniam, quis nostrud exercitation ullamco laboris nisi ut aliquip ex ea commodo consequat.</p>
    <p>Consectetur adipiscing elit, sed do eiusmod tempor incididunt ut labore et dolore magna aliqua. Ut enim ad minim veniam, quis nostrud exercitation ullamco laboris nisi ut aliquip ex ea commodo consequat. Duis aute irure dolor in reprehenderit in voluptate velit esse cillum dolore eu fugiat nulla.</p>
    <p>Lorem ipsum dolor sit amet, consectetur adipiscing elit, sed do eiusmod tempor incididunt ut labore et dolore magna aliqua. Ut enim ad minim veniam, quis nostrud exercitation ullamco laboris nisi ut aliquip ex ea commodo.</p>
  </div>
  <span class="btn">LEARN MORE</span>
</section>

<h2 class="section-title" style="top:1560px">OUR SERVICES</h2>
<section class="services">
  <div class="service">
    <div class="fill" role="img" aria-label="Photo of a teacher and child working on a learning activity" style="background:linear-gradient(135deg,#8fb0a4,#d8b595 60%,#6f6558)"></div>
    <div class="scrim"></div>
    <svg width="44" height="36" viewBox="0 0 44 36" fill="none" stroke="#fff" stroke-width="2.5"><path d="M4 8l18-6 18 6-18 6z"/><path d="M11 11v10c6 5 16 5 22 0V11"/><path d="M40 8v12"/></svg>
    <div class="label">Educational</div>
  </div>
  <div class="service">
    <div class="fill" role="img" aria-label="Photo of a woman preparing a healthy meal in a kitchen" style="background:linear-gradient(135deg,#d9c3ab,#b98d6d 55%,#5e4a3d)"></div>
    <div class="scrim"></div>
    <svg width="36" height="40" viewBox="0 0 36 40" fill="none" stroke="#fff" stroke-width="2.5"><path d="M18 12c-6-4-15-1-15 10 0 9 6 16 10 16 2 0 3-1 5-1s3 1 5 1c4 0 10-7 10-16 0-11-9-14-15-10z"/><path d="M18 12c0-5 3-8 7-9"/></svg>
    <div class="label">Nutritional</div>
  </div>
  <div class="service">
    <div class="fill" role="img" aria-label="Photo of a child receiving a dental check-up" style="background:linear-gradient(135deg,#c9dbe2,#9bb5c2 50%,#5d7482)"></div>
    <div class="scrim"></div>
    <svg width="38" height="40" viewBox="0 0 38 40" fill="none" stroke="#fff" stroke-width="2.5"><path d="M19 8c-4-5-16-5-16 6 0 6 3 9 4 14 1 6 2 10 5 10s3-10 7-10 4 10 7 10 4-4 5-10c1-5 4-8 4-14 0-11-12-11-16-6z"/></svg>
    <div class="label">Dental health</div>
  </div>
  <div class="service">
    <div class="fill" role="img" aria-label="Photo of a mother and child sharing a specialized care session" style="background:linear-gradient(135deg,#e6e2d6,#d3ad8a 55%,#7b6a5c)"></div>
    <div class="scrim"></div>
    <svg width="42" height="38" viewBox="0 0 42 38" fill="none" stroke="#fff" stroke-width="2.5"><path d="M21 35S4 24 4 13C4 6 9 3 13 3c4 0 7 3 8 6 1-3 4-6 8-6 4 0 9 3 9 10 0 11-17 22-17 22z"/></svg>
    <div class="label">Specialized services</div>
  </div>
</section>

<h2 class="section-title" style="top:2052px">OUR TESTIMONIALS</h2>
<span class="arrow" style="left:46px;top:2252px">&#8249;</span>
<span class="arrow" style="left:1140px;top:2252px">&#8250;</span>
<article class="testimonial" style="left:108px">
  <p>Lorem ipsum dolor sit amet, consectetur adipiscing elit, sed do eiusmod tempor incididunt ut labore et dolore magna aliqua. Ut enim ad minim veniam, quis nostrud exercitation ullamco laboris nisi ut aliquip.</p>
  <div class="tag">Lorem ipsum dolor sit amet consectetur</div>
  <div class="person"><div class="avatar" role="img" aria-label="Portrait of the reviewer"></div><div><h4>Elena</h4><div class="stars">★★★★★</div></div></div>
</article>
<article class="testimonial" style="left:442px">
  <p>Lorem ipsum dolor sit amet, consectetur adipiscing elit, sed do eiusmod tempor incididunt ut labore et dolore magna aliqua. Ut enim ad minim veniam, quis nostrud exercitation ullamco laboris nisi ut aliquip.</p>
  <div class="tag">Lorem ipsum dolor sit amet consectetur</div>
  <div class="person"><div class="avatar" role="img" aria-label="Portrait of the reviewer"></div><div><h4>Elena</h4><div class="stars">★★★★★</div></div></div>
</article>
<article class="testimonial" style="left:776px">
  <p>Lorem ipsum dolor sit amet, consectetur adipiscing elit, sed do eiusmod tempor incididunt ut labore et dolore magna aliqua. Ut enim ad minim veniam, quis nostrud exercitation ullamco laboris nisi ut aliquip.</p>
  <div class="tag">Lorem ipsum dolor sit amet consectetur</div>
  <div class="person"><div class="avatar" role="img" aria-label="Portrait of the reviewer"></div><div><h4>Elena</h4><div class="stars">★★★★★</div></div></div>
</article>

<section class="blog">
  <h2>OUR BLOG</h2>
  <span class="side" style="left:46px">&#8249;</span>
  <span class="side" style="left:1140px">&#8250;</span>
  <div class="feature-photo" role="img" aria-label="Photo of a toddler playing with a wooden activity cube"></div>
  <div class="feature-card">
    <h3>Lorem ipsum dolor sit amet, consectetur adipiscing elit</h3>
    <p>Sed ut perspiciatis unde omnis iste natus error sit voluptatem accusantium doloremque.</p>
    <div class="feature-go"><svg width="42" height="42" viewBox="0 0 42 42" fill="none" stroke="#fff" stroke-width="3"><path d="M18 14l7 7-7 7"/></svg></div>
  </div>
  <article class="post" style="top:168px">
    <div class="thumb" role="img" aria-label="Photo of a child reading with a parent" style="background:linear-gradient(135deg,#d6c6b2,#a58368)"></div>
    <div class="text">
      <div class="date"><svg width="12" height="12" viewBox="0 0 12 12" fill="none" stroke="#1fb89a" stroke-width="1.5"><rect x="1" y="2" width="10" height="9"/><path d="M1 5h10M4 0v3M8 0v3"/></svg>Jun 06, 2024</div>
      <h3>Lorem ipsum dolor sit amet, consectetur</h3>
      <p>Sed ut perspiciatis unde omnis iste natus error sit voluptatem accusantium.</p>
      <div class="readmore">READ MORE &#8250;</div>
    </div>
  </article>
  <article class="post" style="top:392px">
    <div class="thumb" role="img" aria-label="Photo of a smiling child with a caregiver" style="background:linear-gradient(135deg,#c7d2d6,#b8957a)"></div>
    <div class="text">
      <div class="date"><svg width="12" height="12" viewBox="0 0 12 12" fill="none" stroke="#1fb89a" stroke-width="1.5"><rect x="1" y="2" width="10" height="9"/><path d="M1 5h10M4 0v3M8 0v3"/></svg>Jun 06, 2024</div>
      <h3>Lorem ipsum dolor sit amet, consectetur</h3>
      <p>Sed ut perspiciatis unde omnis iste natus error sit voluptatem accusantium.</p>
      <div class="readmore">READ MORE &#8250;</div>
    </div>
  </article>
</section>

<footer class="site-footer">
  <div class="brand">TALMA</div>
  <div class="col" style="left:362px">
    <h4>QUICK LINKS</h4>
    <ul><li>Home</li><li>About Us</li><li>Services</li><li>Blog</li><li>Contact</li></ul>
  </div>
  <div class="col contact" style="left:562px">
    <h4>CONTACT US</h4>
    <ul>
      <li><span class="ico"><svg width="12" height="12" viewBox="0 0 12 12" fill="#fff"><path d="M2 1h2l1 3-1.5 1a7 7 0 003.5 3.5L8 7l3 1v2a1 1 0 01-1 1A9 9 0 011 2a1 1 0 011-1z"/></svg></span>(757) 555-0142</li>
      <li><span class="ico"><svg width="12" height="10" viewBox="0 0 12 10" fill="none" stroke="#fff" stroke-width="1.3"><rect x=".7" y=".7" width="10.6" height="8.6"/><path d="M1 1l5 4 5-4"/></svg></span>hello@talma.org</li>
      <li><span class="ico"><svg width="10" height="12" viewBox="0 0 10 12" fill="#fff"><path d="M5 0a4 4 0 014 4c0 3-4 8-4 8S1 7 1 4a4 4 0 014-4zm0 2.5a1.5 1.5 0 100 3 1.5 1.5 0 000-3z"/></svg></span><span>1200 Harbor Lane, Norfolk,<br>VA 23510</span></li>
      <li><span class="ico"><svg width="12" height="12" viewBox="0 0 12 12" fill="none" stroke="#fff" stroke-width="1.3"><rect x="1" y="4" width="10" height="6"/><path d="M3 4V1h6v3"/></svg></span>(757) 555-0198</li>
    </ul>
  </div>
  <div class="col subscribe" style="left:830px">
    <h4>SUBSCRIBE TO OUR BLOG</h4>
    <p>Sign up today to get updates on how to support families and children in our community.</p>
    <div class="field">Enter email address<span class="send"></span></div>
    <div class="socials"><span></span><span class="on"></span><span></span><span></span></div>
  </div>
</footer>
<div class="chat"></div>
<div class="legal">
  <div class="left">Copyright© 2024 <b>TALMA</b>  |  All Rights Reserved</div>
  <div class="right">Specifications | Site Map | Privacy Policy</div>
</div>

</body>
</html>
```